REAL ESTATE MAILBOX DROP FLYER

I am looking for two flyer designs. One for DL and one for A4 size. My company is a boutique real estate agency that offers a full/high quality service at a very low commission rate.

Key Phrases to be included

A4 Design should have a space for some text and a table in the center (outline below)

Target Market(s)

Home Owners

Industry/Entity Type

Real Estate Agent

Colors
0455a3

Requirements
Must have
• Eye Catching
• Bold
• high end feel
• Color pallette should match the logo
• The feel of the brochures must convey a trustworthy, high end service.
• Must be eye catching and easy to read
• Editable file formats must be supplied

```html
<!DOCTYPE html>
<html lang="en">
<head>
<meta charset="utf-8">
<title>Low Rate Estates – Mailbox Flyers</title>
<link href="https://fonts.googleapis.com/css2?family=Questrial&family=Roboto+Condensed:ital,wght@0,400;0,700;1,700&family=Roboto:wght@400;500;700&display=swap" rel="stylesheet">
<style>
  :root {
    --brand-blue: #0455a3;
    --navy: #13284d;
    --copper: #c0865a;
    --ink: #2b2b2b;
    --paper: #ffffff;
    --stage: #efefef;
    --sky-top: #3f7fc4;
    --sky-mid: #8cb8e4;
  }
  * { margin: 0; padding: 0; box-sizing: border-box; }
  html, body { width: 1200px; height: 1000px; overflow: hidden; }
  body {
    background: linear-gradient(#fafafa, var(--stage));
    font-family: "Roboto", Arial, sans-serif;
    color: var(--ink);
    position: relative;
  }
  .flyer {
    position: absolute;
    background: var(--paper);
    box-shadow: 0 4px 14px rgba(0,0,0,.25);
    overflow: hidden;
  }
  .flyer--dl { left: 94px; top: 296px; width: 304px; height: 682px; }
  .flyer--a4 { left: 418px; top: 14px; width: 684px; height: 954px; }
  .abs { position: absolute; }

  .hero-photo {
    position: absolute; left: 0; top: 0; width: 100%;
    background: linear-gradient(180deg, var(--sky-top) 0%, var(--sky-mid) 38%, #a9a096 55%, #7d6e60 72%, #c9c3b5 84%, #6c8d45 100%);
  }
  .headline { position: absolute; color: #fff; font-family: "Questrial", "Century Gothic", sans-serif; line-height: 1; text-shadow: 0 1px 3px rgba(0,0,0,.2); }
  .headline .save { font-weight: 700; -webkit-text-stroke: 1px #fff; }
  .divider { position: absolute; left: 0; width: 100%; background: var(--navy); }

  .banner { position: absolute; background: var(--brand-blue); color: #fff; font-family: "Roboto Condensed", sans-serif; }
  .banner .rate { color: var(--copper); font-weight: 700; font-family: "Roboto", sans-serif; letter-spacing: -2px; }
  .banner-tail { position: absolute; }

  .gallery { position: absolute; background: var(--navy); }
  .gallery .photo { position: absolute; border: 2px solid #fff; }
  .photo--dusk { background: linear-gradient(180deg, #b9a5d6 0%, #e3a7b5 40%, #5a6b9a 70%, #8da0b7 100%); }
  .photo--day { background: linear-gradient(180deg, #9cc4ea 0%, #d8e4ee 40%, #6b6355 65%, #6d8d3c 100%); }
  .photo--sunset { background: linear-gradient(180deg, #e59aa6 0%, #f4b7a4 38%, #a88e78 65%, #5d8136 100%); }

  .feature { position: absolute; left: 93px; width: 342px; }
  .feature h3 { font-family: "Roboto Condensed", sans-serif; font-weight: 700; font-size: 15px; color: var(--brand-blue); line-height: 1.1; }
  .feature p { font-size: 12px; line-height: 1.25; text-align: justify; }
  .feature-mark { position: absolute; left: 64px; }

  .contact-title { position: absolute; font-size: 19px; color: #333; white-space: nowrap; }
  .contact-title b { font-weight: 700; }
  .contact-title .offer { font-family: "Roboto", sans-serif; font-style: italic; font-weight: 700; color: var(--brand-blue); border-bottom: 2px solid var(--navy); padding-bottom: 1px; }
  .contact-row { position: absolute; display: flex; align-items: center; white-space: nowrap; }
  .contact-row svg { flex: none; }

  .wordmark { position: absolute; font-family: "Roboto Condensed", sans-serif; font-weight: 400; color: var(--navy); text-align: center; line-height: 1; letter-spacing: 1px; }

  .footer-bar { position: absolute; left: 0; width: 100%; background: var(--navy); color: #fff; text-align: center; font-weight: 500; letter-spacing: 1px; }
</style>
</head>
<body>

<!-- DL flyer -->
<article class="flyer flyer--dl">
  <div class="hero-photo" style="height:364px" role="img" aria-label="Large brick and stone family home under a blue sky with clouds"></div>
  <h1 class="headline" style="left:24px;top:72px">
    <span class="save" style="font-size:40px">SAVE</span><span style="font-size:20px"> thousands on</span><br>
    <span class="save" style="font-size:35px">COMMISSIONS!</span>
  </h1>
  <div class="divider" style="top:360px;height:4px"></div>

  <div class="banner" style="left:24px;top:289px;width:138px;height:128px;text-align:center">
    <div style="font-size:13px;margin-top:17px">Full Service Agency,</div>
    <div class="rate" style="font-size:50px;line-height:50px">1%</div>
    <div style="font-size:19px;font-weight:700;line-height:20px">COMMISSION</div>
  </div>
  <svg class="banner-tail" style="left:100px;top:417px" width="62" height="28" viewBox="0 0 62 28"><polygon points="0,10 62,0 62,28" fill="var(--navy)"/></svg>

  <div class="gallery" style="left:189px;top:327px;width:102px;height:217px">
    <div class="photo photo--dusk" style="left:6px;top:9px;width:90px;height:61px" role="img" aria-label="Blue two-storey house at dusk"></div>
    <div class="photo photo--day" style="left:6px;top:79px;width:90px;height:61px" role="img" aria-label="Country home with porch and lawn"></div>
    <div class="photo photo--sunset" style="left:6px;top:149px;width:90px;height:61px" role="img" aria-label="Suburban home at sunset"></div>
  </div>

  <p class="abs" style="left:26px;top:474px;font-size:14px">Contact <b>Marcus</b> today!</p>
  <div class="abs" style="left:26px;top:492px;width:132px;height:21px;border:1.5px dashed #777;border-radius:5px;display:flex;align-items:center;justify-content:center;gap:5px;color:var(--copper);font-weight:700;font-size:16px">
    <svg width="12" height="12" viewBox="0 0 24 24"><path d="M6.6 10.8a15 15 0 0 0 6.6 6.6l2.2-2.2c.3-.3.7-.4 1-.2 1.1.4 2.3.6 3.6.6.6 0 1 .4 1 1V20c0 .6-.4 1-1 1A17 17 0 0 1 3 4c0-.6.4-1 1-1h3.5c.6 0 1 .4 1 1 0 1.3.2 2.5.6 3.6.1.3 0 .7-.2 1z" fill="var(--copper)"/></svg>
    0400 123 456
  </div>
  <p class="abs" style="left:26px;top:517px;font-size:12.5px">for a <b style="color:var(--brand-blue);font-style:italic">FREE APPRAISAL!</b></p>

  <p class="abs" style="left:24px;top:560px;font-family:'Roboto Condensed',sans-serif;font-weight:700;font-size:13px">More Money in YOUR Pocket!</p>
  <div class="contact-row" style="left:24px;top:582px;font-size:9px;gap:6px">
    <svg width="11" height="11" viewBox="0 0 20 20"><circle cx="10" cy="10" r="10" fill="var(--copper)"/><circle cx="10" cy="7.5" r="3" fill="#fff"/><path d="M4.5 15a5.5 4 0 0 1 11 0z" fill="#fff"/></svg>Marcus Hale</div>
  <div class="contact-row" style="left:24px;top:601px;font-size:9px;gap:6px">
    <svg width="11" height="11" viewBox="0 0 20 20"><circle cx="10" cy="10" r="10" fill="var(--copper)"/><path d="M7.3 9.7a7 7 0 0 0 3 3l1-1c.2-.2.4-.2.5-.1l1.7.3c.3 0 .4.2.4.5v1.4c0 .3-.2.5-.5.5A8 8 0 0 1 5.5 6.4c0-.3.2-.5.5-.5h1.4c.3 0 .5.2.5.4l.3 1.7c0 .2 0 .4-.1.5z" fill="#fff"/></svg>0400 123 456</div>
  <div class="contact-row" style="left:24px;top:620px;font-size:9px;gap:6px">
    <svg width="11" height="11" viewBox="0 0 20 20"><circle cx="10" cy="10" r="10" fill="var(--copper)"/><rect x="5" y="6.5" width="10" height="7" fill="none" stroke="#fff" stroke-width="1.2"/><path d="M5 6.5l5 4 5-4" fill="none" stroke="#fff" stroke-width="1.2"/></svg>marcus@lowrateestates.com.au</div>

  <div class="wordmark" style="left:192px;top:575px;width:96px;font-size:16px">LOW RATE<br>ESTATES</div>

  <div class="footer-bar" style="top:646px;height:20px;font-size:11px;line-height:20px">www.lowrateestates.com.au</div>
</article>

<!-- A4 flyer -->
<article class="flyer flyer--a4">
  <div class="hero-photo" style="height:426px" role="img" aria-label="Large brick and stone family home with gabled roofs and double garage under a blue sky"></div>
  <h1 class="headline" style="left:97px;top:38px">
    <span class="save" style="font-size:50px">SAVE</span><span style="font-size:25px"> thousands on</span><br>
    <span class="save" style="font-size:50px;margin-left:133px">COMMISSIONS!</span>
  </h1>
  <div class="divider" style="top:423px;height:5px"></div>

  <div class="banner" style="left:68px;top:397px;width:320px;height:116px">
    <div class="rate abs" style="left:12px;top:8px;font-size:86px;line-height:100px">1%</div>
    <div class="abs" style="left:120px;top:30px;font-size:20px">Full Service Agency,</div>
    <div class="abs" style="left:118px;top:54px;font-size:33px;font-weight:700">COMMISSION</div>
  </div>
  <svg class="banner-tail" style="left:248px;top:513px" width="140" height="24" viewBox="0 0 140 24"><polygon points="0,24 140,0 140,20 30,22" fill="var(--navy)"/></svg>

  <div class="gallery" style="left:454px;top:371px;width:202px;height:430px">
    <div class="photo photo--dusk" style="left:10px;top:16px;width:182px;height:121px" role="img" aria-label="Blue two-storey house at dusk"></div>
    <div class="photo photo--day" style="left:10px;top:154px;width:182px;height:117px" role="img" aria-label="Country home with porch and green lawn"></div>
    <div class="photo photo--sunset" style="left:10px;top:288px;width:182px;height:123px" role="img" aria-label="Suburban home under a pink sunset sky"></div>
  </div>

  <svg class="feature-mark" style="top:550px" width="16" height="16" viewBox="0 0 20 20"><circle cx="10" cy="10" r="10" fill="var(--copper)"/><path d="M5.5 10.5l3 3 6-6.5" fill="none" stroke="#fff" stroke-width="2"/></svg>
  <section class="feature" style="top:549px">
    <h3>Trained Negotiator</h3>
    <p>With over ten years of sales and negotiation training we will work tirelessly with you and your buyers to ensure you get the best possible price for your house.</p>
  </section>

  <svg class="feature-mark" style="top:626px" width="16" height="16" viewBox="0 0 20 20"><circle cx="10" cy="10" r="10" fill="var(--copper)"/><path d="M5.5 10.5l3 3 6-6.5" fill="none" stroke="#fff" stroke-width="2"/></svg>
  <section class="feature" style="top:625px">
    <h3>Total Focus</h3>
    <p>In order to maintain the highest level of customer service we limit our business to a maximum of five clients at a time. This will allow us to give your home the time and attention it deserves.</p>
  </section>

  <svg class="feature-mark" style="top:708px" width="16" height="16" viewBox="0 0 20 20"><circle cx="10" cy="10" r="10" fill="var(--copper)"/><path d="M5.5 10.5l3 3 6-6.5" fill="none" stroke="#fff" stroke-width="2"/></svg>
  <section class="feature" style="top:707px">
    <h3>One Percent Commissions</h3>
    <p>Our low cost model removes expensive overheads and allows us to deliver a high-end service while only charging a 1% commission!</p>
  </section>

  <p class="contact-title" style="left:24px;top:806px">Contact <b>Marcus</b> today for a <span class="offer">FREE APPRAISAL!</span></p>
  <div class="contact-row" style="left:26px;top:841px;font-size:15px;gap:11px">
    <svg width="17" height="17" viewBox="0 0 20 20"><circle cx="10" cy="10" r="10" fill="var(--copper)"/><circle cx="10" cy="7.5" r="3" fill="#fff"/><path d="M4.5 15a5.5 4 0 0 1 11 0z" fill="#fff"/></svg>Marcus Hale</div>
  <div class="contact-row" style="left:26px;top:868px;font-size:15px;gap:11px">
    <svg width="17" height="17" viewBox="0 0 20 20"><circle cx="10" cy="10" r="10" fill="var(--copper)"/><path d="M7.3 9.7a7 7 0 0 0 3 3l1-1c.2-.2.4-.2.5-.1l1.7.3c.3 0 .4.2.4.5v1.4c0 .3-.2.5-.5.5A8 8 0 0 1 5.5 6.4c0-.3.2-.5.5-.5h1.4c.3 0 .5.2.5.4l.3 1.7c0 .2 0 .4-.1.5z" fill="#fff"/></svg>0400 123 456</div>
  <div class="contact-row" style="left:26px;top:895px;font-size:15px;gap:11px">
    <svg width="17" height="17" viewBox="0 0 20 20"><circle cx="10" cy="10" r="10" fill="var(--copper)"/><rect x="5" y="6.5" width="10" height="7" fill="none" stroke="#fff" stroke-width="1.2"/><path d="M5 6.5l5 4 5-4" fill="none" stroke="#fff" stroke-width="1.2"/></svg>marcus@lowrateestates.com.au</div>

  <div class="wordmark" style="left:462px;top:852px;width:192px;font-size:32px">LOW RATE<br>ESTATES</div>

  <div class="footer-bar" style="top:931px;height:23px;font-size:13px;line-height:23px">www.lowrateestates.com.au</div>
</article>

</body>
</html>
```